Business Card Revision

Need to redesign my business cards for a new professional look. We are a courier company. You can go to www.qvrunners.com to see what we do. The trucks have an old company name (Sprout) on them but that is the company we are just now
changing the name.

Target Market(s)

Potential clients. We service the automotive, plumbing, printing, air freight industries as well as many others.

Industry/Entity Type

Business

Contact Information for Business Card

QVmotion
20864 Lark Fenmore Parkway
Cincinnati, Oh 45873

Thomas R. Wendall
President

tom@qvrunners.com

Main: (513) 555-0147

```html
<!DOCTYPE html>
<html lang="en">
<head>
<meta charset="utf-8">
<title>QVmotion Business Card</title>
<link href="https://fonts.googleapis.com/css2?family=Open+Sans:wght@400;600;700;800&display=swap" rel="stylesheet">
<style>
  :root {
    --page-bg: #e9e6e1;
    --card-white: #f7f8f8;
    --brand-blue: #1a9ad6;
    --blue-light: #21b0e6;
    --blue-dark: #0f7cc0;
    --brand-green: #3dbb4f;
    --text-light: #ffffff;
  }
  html, body {
    margin: 0;
    padding: 0;
    width: 1200px;
    height: 780px;
    overflow: hidden;
    background: var(--page-bg);
  }
  .canvas {
    position: relative;
    width: 1200px;
    height: 780px;
  }
  .business-card {
    position: absolute;
    left: 180px;
    top: 150px;
    width: 840px;
    height: 480px;
    display: flex;
    box-shadow: 0 10px 30px rgba(0,0,0,0.18);
    font-family: "Open Sans", Arial, sans-serif;
  }
  .brand-panel {
    width: 400px;
    background: var(--card-white);
    display: flex;
    align-items: center;
    justify-content: center;
  }
  .brand-name {
    display: flex;
    align-items: center;
    gap: 16px;
    color: var(--brand-blue);
    font-weight: 800;
    font-size: 44px;
    letter-spacing: 1px;
    text-transform: uppercase;
  }
  .brand-square {
    width: 26px;
    height: 26px;
    background: var(--brand-green);
  }
  .divider {
    width: 5px;
    background: var(--brand-green);
  }
  .contact-panel {
    flex: 1;
    background: linear-gradient(160deg, var(--blue-light) 0%, var(--brand-blue) 55%, var(--blue-dark) 100%);
    color: var(--text-light);
    padding: 0 0 0 56px;
    display: flex;
    flex-direction: column;
    justify-content: center;
  }
  .person-name {
    margin: 0;
    font-size: 32px;
    font-weight: 700;
    line-height: 1.1;
  }
  .person-title {
    margin: 2px 0 30px;
    font-size: 20px;
    font-weight: 400;
  }
  .address {
    margin: 0 0 8px;
    font-style: normal;
    font-size: 19px;
    line-height: 1.35;
  }
  .contact-line {
    display: flex;
    align-items: center;
    gap: 10px;
    font-size: 19px;
    line-height: 1.5;
  }
  .contact-icon {
    width: 20px;
    height: 20px;
    flex: none;
  }
  .website {
    margin-top: 22px;
    font-size: 21px;
    font-weight: 700;
  }
</style>
</head>
<body>
<main class="canvas">
  <section class="business-card">
    <div class="brand-panel">
      <div class="brand-name">
        <span class="brand-square"></span>
        <span>QV Runners</span>
      </div>
    </div>
    <div class="divider"></div>
    <div class="contact-panel">
      <h1 class="person-name">Thomas R. Wendall</h1>
      <p class="person-title">President</p>
      <address class="address">
        20864 Lark Fenmore Parkway<br>
        Cincinnati, Oh 45873
      </address>
      <div class="contact-line">
        <svg class="contact-icon" viewBox="0 0 20 20" aria-hidden="true">
          <rect width="20" height="20" rx="2" fill="#ffffff"/>
          <path d="M6 4.5c.6-.5 1.4-.4 1.8.2l1 1.6c.3.5.2 1.1-.2 1.5l-.8.7c.6 1.3 1.6 2.4 2.9 3l.7-.8c.4-.4 1-.5 1.5-.2l1.6 1c.6.4.7 1.2.2 1.8l-.8.9c-.7.7-1.8.9-2.7.5C8.3 14.2 5.8 11.7 4.3 8.8c-.4-.9-.2-2 .5-2.7z" fill="var(--brand-blue)"/>
        </svg>
        <span>(513) 555-0147</span>
      </div>
      <div class="contact-line">
        <svg class="contact-icon" viewBox="0 0 20 20" aria-hidden="true">
          <rect width="20" height="20" rx="2" fill="#ffffff"/>
          <rect x="4" y="6" width="12" height="8.5" fill="none" stroke="var(--brand-blue)" stroke-width="1.5"/>
          <path d="M4 6l6 5 6-5" fill="none" stroke="var(--brand-blue)" stroke-width="1.5"/>
        </svg>
        <span>tom@qvrunners.com</span>
      </div>
      <div class="website">www.qvrunners.com</div>
    </div>
  </section>
</main>
</body>
</html>
```